Rota sem falha

We need a web design for a new company based in João Pessoa, Brazil, called Rota Sem Falha (Smooth Route). After the client/consumer fullfill a questionary about the wanted destination, personal interests and available budget for the trip, we aim to plan a personalized travel guide for that independent travellers, containing informations about the places we suggest them to visit, amount of days indicated in each city, possibles restaurants and hotels. The site will help people to manage their budgets and optimize the time at their travel at a low cost and in a simple way. We would like to see clean and sophisticated design that use colors in shades of black, grey and white (and perhaps a touch of pink - what do you think?). The final design should communicate safety, professionalism and experience.
Target Market(s)
People who dont like to buy excursion packages but think they could need a consultance in planning their trip
Industry/Entity Type
It Company
Requirements
Must have
- The menu shall indicate the following points (that will lead to new pages):
1-Our Services
2-Prices
2- FAQ
3-Hire a travel expert to plan your trip!
4-Around the world - blog
Fell free to put the logo of the site "Rota Sem Falha" in the top middle/top left/ or wherever you find it is more appropriate.
On the top right we should put a login/register button.
Above that menu, I thought about illustrating with a figure demonstrating how it works - step by step, as seen in the link http://trekzio.com/ - but in a more clean design.
Nice to have
- Coin ferry will be used as the payment option.

```html
<!DOCTYPE html>
<html lang="en">
<head>
<meta charset="utf-8">
<title>Rota Sem Falha</title>
<link href="https://fonts.googleapis.com/css2?family=PT+Sans:ital,wght@0,400;0,700;1,400&family=Roboto+Condensed:wght@400;700&display=swap" rel="stylesheet">
<style>
:root{
  --pink:#e8127f;
  --charcoal:#3b3b3b;
  --charcoal-dark:#2f2f2f;
  --step:#8a8a8a;
  --step-dark:#6f6f6f;
  --ink:#3a3a3a;
  --body:#5a5a5a;
  --soft:#f1f1f1;
  --footer:#0d0d0d;
  --white:#ffffff;
}
*{margin:0;padding:0;box-sizing:border-box}
html,body{width:952px;height:1200px;overflow:hidden;background:var(--white)}
body{position:relative;font-family:Arial,Helvetica,sans-serif;color:var(--body)}
.abs{position:absolute}

/* header */
.site-header{position:absolute;left:0;top:0;width:952px;height:113px;background:var(--charcoal);border-top:3px solid var(--pink)}
.brand{position:absolute;left:104px;top:38px;font-family:"PT Sans",sans-serif;font-weight:700;font-size:32px;color:var(--white);letter-spacing:.5px}
.account-tab{position:absolute;left:706px;top:0;width:122px;height:24px;background:var(--pink);clip-path:polygon(0 0,100% 0,94% 100%,5% 100%);font-family:"Roboto Condensed",sans-serif;font-size:11px;color:var(--white);display:flex;align-items:center;justify-content:center;gap:8px}
.cta-title{position:absolute;left:413px;top:14px;font-family:"PT Sans",sans-serif;font-size:17px;color:var(--white)}
.steps{position:absolute;left:414px;top:44px}
.step-label{position:absolute;top:0;width:80px;font-family:"Roboto Condensed",sans-serif;color:var(--white);text-align:left}
.step-label b{display:block;font-size:16px;font-weight:400;margin-top:10px}
.step-label span{display:block;font-family:Arial,sans-serif;font-size:9px;margin-top:1px}

/* nav */
.main-nav{position:absolute;left:0;top:113px;width:952px;height:43px;background:linear-gradient(#ffffff,#e6e6e6);border-bottom:1px solid #cfcfcf;display:flex;align-items:center;padding-left:113px}
.main-nav a{font-family:"Roboto Condensed",sans-serif;font-size:14px;color:#2b2b2b;text-decoration:none;padding:0 22px;border-left:1px solid #d2d2d2;line-height:22px}
.main-nav a:first-child{border-left:none;padding-left:0}
.main-nav a:last-child{padding-right:0}

/* hero */
.hero{position:absolute;left:0;top:156px;width:952px;height:411px;background:#efefef}
.hero-frame{position:absolute;left:110px;top:16px;width:730px;height:347px;background:var(--white);box-shadow:0 4px 8px rgba(0,0,0,.12)}
.hero-photo{position:absolute;left:8px;top:7px;width:713px;height:329px;background:linear-gradient(100deg,#c9bfb2 0%,#6d6a68 25%,#dcdcd6 52%,#eef0e6 70%,#b9c4a8 88%,#7f8a6c 100%)}
.hero-strip{position:absolute;left:390px;top:150px;width:323px;height:95px;background:linear-gradient(90deg,rgba(255,255,255,0),rgba(255,255,255,.7) 30%)}
.hero-title{position:absolute;right:22px;top:158px;font-family:"PT Sans",sans-serif;font-weight:700;font-size:40px;color:var(--ink);letter-spacing:1px}
.hero-sub{position:absolute;right:29px;top:205px;font-family:"PT Sans",sans-serif;font-style:italic;font-size:15px;color:var(--pink)}
.hero-button{position:absolute;left:587px;top:260px;width:219px;height:44px;border-radius:22px;background:linear-gradient(#ffffff,#c9c9c9);border:1px solid #9d9d9d;font-family:"PT Sans",sans-serif;font-weight:700;font-size:22px;color:var(--ink);display:flex;align-items:center;justify-content:center;box-shadow:0 2px 4px rgba(0,0,0,.25)}
.slider-dots{position:absolute;left:396px;top:380px;display:flex;align-items:center;gap:8px}
.dot{width:16px;height:16px;border-radius:50%;background:#666;box-shadow:inset 0 2px 3px rgba(0,0,0,.4)}
.dot.active{background:var(--pink)}

/* content */
.section-title{font-family:"PT Sans",sans-serif;font-weight:700;font-size:26px;color:var(--ink)}
.overview{position:absolute;left:113px;top:592px;width:444px}
.overview p{font-size:11px;line-height:16px;text-align:justify;margin-top:16px}
.overview p+p{margin-top:16px}
.how{position:absolute;left:581px;top:592px}
.video-box{position:absolute;left:0;top:45px;width:251px;height:180px;background:#f3f3f3;border:1px solid #dcdcdc;padding:5px}
.video-still{width:100%;height:100%;background:linear-gradient(120deg,#4a4a4a,#9a9a9a 45%,#dadada 70%,#5e5e5e);display:flex;align-items:center;justify-content:center}

/* testimonials */
.testimonials{position:absolute;left:115px;top:860px;width:689px}
.testimonials .rule{position:absolute;top:18px;height:5px;background:repeating-linear-gradient(135deg,#ddd 0 1px,#fff 1px 3px)}
.testimonials .section-title{text-align:center}
.quote-text{position:absolute;left:80px;top:56px;width:530px;text-align:center;font-size:11.5px;line-height:20.5px;color:#666}
.author{position:absolute;left:0;top:126px;width:689px;text-align:center;font-size:11px;font-weight:700;color:#222}
.newsletter{position:absolute;left:115px;top:1025px;width:689px;height:74px;background:#f6f6f6}
.newsletter .mark{position:absolute;left:26px;top:14px;font-family:Georgia,serif;font-size:54px;color:#bbb;line-height:1}
.newsletter .excerpt{position:absolute;left:63px;top:21px;width:335px;font-style:italic;font-size:11px;line-height:15.5px;color:#999}
.newsletter .divider{position:absolute;left:427px;top:15px;width:1px;height:46px;background:#d6d6d6}
.email-field{position:absolute;left:443px;top:27px;width:155px;height:21px;background:var(--white);border:1px solid #e3e3e3;font-style:italic;font-size:7px;color:#999;padding:7px 0 0 8px}
.submit{position:absolute;left:597px;top:27px;width:55px;height:21px;background:#1b1b1b;color:var(--white);font-size:8px;font-weight:700;display:flex;align-items:center;justify-content:center}

/* footer */
.site-footer{position:absolute;left:0;top:1120px;width:952px;height:80px;background:var(--footer);color:#e9e9e9;font-size:10px}
.footer-links{position:absolute;left:118px;top:25px;word-spacing:1px}
.footer-links span{margin:0 9px}
.copyright{position:absolute;left:118px;top:44px}
.verified-badge{position:absolute;left:648px;top:20px;width:47px;height:47px;border-radius:50%;background:radial-gradient(#f3d25a,#d7a826);border:2px solid #f8e38b}
.pay-name{position:absolute;left:728px;top:20px;font-family:"PT Sans",sans-serif;font-weight:700;font-size:17px;color:var(--white)}
.cards{position:absolute;left:706px;top:43px;display:flex;gap:3px}
.card{width:25px;height:15px;border-radius:2px;background:#d0d0d0}
.card:nth-child(2){background:#1d3f8f}
.card:nth-child(3){background:#5a8fc9}
.card:nth-child(4){background:#eeeeee}
</style>
</head>
<body>

<header class="site-header">
  <div class="brand">Rota Sem Falha</div>
  <div class="account-tab"><span>Login</span><span>|</span><span>Register</span></div>
  <div class="cta-title">Get Started Now!</div>
  <div class="steps">
    <svg class="abs" style="left:0;top:0" width="420" height="55" viewBox="0 0 420 55">
      <defs>
        <linearGradient id="stepFill" x1="0" y1="0" x2="0" y2="1">
          <stop offset="0" stop-color="#9a9a9a"/><stop offset="1" stop-color="#747474"/>
        </linearGradient>
      </defs>
      <polygon points="0,0 70,0 96,27.5 70,55 0,55" fill="url(#stepFill)"/>
      <polygon points="70,0 152,0 178,27.5 152,55 70,55 96,27.5" fill="url(#stepFill)" stroke="#5e5e5e" stroke-width="1"/>
      <polygon points="152,0 234,0 260,27.5 234,55 152,55 178,27.5" fill="url(#stepFill)" stroke="#5e5e5e" stroke-width="1"/>
      <polygon points="234,0 316,0 342,27.5 316,55 234,55 260,27.5" fill="url(#stepFill)" stroke="#5e5e5e" stroke-width="1"/>
      <polygon points="316,0 392,0 418,27.5 392,55 316,55 342,27.5" fill="url(#stepFill)" stroke="#5e5e5e" stroke-width="1"/>
    </svg>
    <div class="step-label" style="left:8px"><b>Generate</b><span>dummy text</span></div>
    <div class="step-label" style="left:97px"><b>Review</b><span>dummy text</span></div>
    <div class="step-label" style="left:182px"><b>Date</b><span>dummy text</span></div>
    <div class="step-label" style="left:263px"><b>Trip</b><span>dummy text</span></div>
    <div class="step-label" style="left:344px"><b>Compare</b><span>dummy text</span></div>
  </div>
</header>

<nav class="main-nav">
  <a>Home</a><a>Our Services</a><a>Prices</a><a>FAQ</a><a>Hire a travel expert</a><a>Around the world - blog</a><a>Contact Us</a>
</nav>

<section class="hero">
  <div class="hero-frame">
    <div class="hero-photo" role="img" aria-label="Photo of travel consultants with a laptop pointing at palm trees">
      <div class="hero-strip"></div>
      <div class="hero-title">Plan your Trip</div>
      <div class="hero-sub">with expert consultants</div>
    </div>
    <div class="hero-button" style="left:587px;top:316px">Get Started Now!</div>
  </div>
  <div class="slider-dots">
    <svg width="14" height="20" viewBox="0 0 14 20"><polyline points="11,2 3,10 11,18" fill="none" stroke="#999" stroke-width="3"/></svg>
    <div class="dot" style="margin-left:12px"></div><div class="dot active"></div><div class="dot"></div><div class="dot"></div>
    <svg width="14" height="20" viewBox="0 0 14 20" style="margin-left:12px"><polyline points="3,2 11,10 3,18" fill="none" stroke="#999" stroke-width="3"/></svg>
  </div>
</section>

<section class="overview">
  <h2 class="section-title">Overview !</h2>
  <p>Praesent vestibulum molestie lacus. Aenean nonummy hendrerit mauris. Phasellus porta. Fusce suscipit varius mi. Cum sociis natoque penatibus et magnis dis parturient montes, nascetur ridiculus mus. Nulla dui. Fusce feugiat malesuada odio. Morbi nunc odio, gravida at, cursus nec, luctus a, lorem. Maecenas tristique orci ac sem. Duis ultricies montes, nascetur ridiculus mus. Nulla dui. Fusce feugiat malesuada odio. Morbi nunc odio, gravida at, cursus nec, luctus a, lorem. Maecenas tristique orci ac sem. Duis ultricies pharetra magna. Donec accumsan malesuada orci.</p>
  <p>Montes, nascetur ridiculus mus. Nulla dui. Fusce feugiat malesuada odio. Morbi nunc odio, gravida at, cursus nec, luctus a, lorem. Maecenas tristique orci ac sem. Duis ultricies montes, nascetur ridiculus mus. Nulla dui.</p>
</section>

<section class="how">
  <h2 class="section-title">How We Work?</h2>
  <div class="video-box">
    <div class="video-still" role="img" aria-label="Black and white video still of travel agents helping a client at a desk">
      <svg width="54" height="54" viewBox="0 0 54 54"><circle cx="27" cy="27" r="26" fill="rgba(0,0,0,.35)"/><polygon points="21,15 40,27 21,39" fill="#eee"/></svg>
    </div>
  </div>
</section>

<section class="testimonials">
  <div class="rule" style="left:0;width:239px"></div>
  <div class="rule" style="left:451px;width:238px"></div>
  <h2 class="section-title">Testimonials</h2>
  <p class="quote-text">At vero eos et accusamus et iusto odio dignissimos ducimus qui blanditiis praesentium voluptatum deleniti atque corrupti quos dolores et quas molestias excepturi sint occaecati cupiditate non provident, similique sunt in culpa qui officia deserunt mollitia animi, id est laborum...</p>
  <svg class="abs" style="left:234px;top:125px" width="12" height="18" viewBox="0 0 12 18"><polyline points="10,2 3,9 10,16" fill="none" stroke="#222" stroke-width="2.2"/></svg>
  <div class="author">Martin Hale, Recife</div>
  <svg class="abs" style="left:443px;top:125px" width="12" height="18" viewBox="0 0 12 18"><polyline points="2,2 9,9 2,16" fill="none" stroke="#222" stroke-width="2.2"/></svg>
</section>

<section class="newsletter">
  <div class="mark">&ldquo;</div>
  <p class="excerpt">At vero eos et accusamus et iusto odio dignimos ducimus qui blanditiis praese ntium voluptatum deleniti atque. Errupti quos dolores et quas...</p>
  <div class="divider"></div>
  <div class="email-field">YOUR E-MAIL</div>
  <div class="submit">SUBMIT</div>
</section>

<footer class="site-footer">
  <div class="footer-links">Home<span>|</span>Our Services<span>|</span>Prices<span>|</span>FAQ<span>|</span>Hire a travel expert<span>|</span>Blog</div>
  <div class="copyright">Copyright © Rota Sem Falha &nbsp;2013 &nbsp;All Rights Reserved</div>
  <div class="verified-badge"></div>
  <div class="pay-name">Coin ferry</div>
  <div class="cards"><div class="card"></div><div class="card"></div><div class="card"></div><div class="card"></div></div>
</footer>

</body>
</html>
```